Banner Ad for Online e-commerce snack shop needs design for their Rivet Bundle Snack Box

We need 2 different size graphic designs that play off the same elements. The first will be a 1280px x 500px slide banner that will be used on the homepage of our website and the second will be an 800px x 800 px square ad that will be used on our box page (http://munchlooptreats.com/collections/taste-boxes) along with advertising on chatterlane. (which means copy only on 20%)

We are selling a snack box that includes 10 awesome, single-serve snacks from the great state of Colorado.

This design should play off the State of Colorado's flag or its icon. (similar to how the Juniper Parcel was done) It should also include in some form or fashion the 10 snacks or the box of snacks.

Please see the prior examples in the files uploaded. More can be seen at our site, munchlooptreats.com. The designs will need to be delivered to us as a PSD and a JPG file. Thank you for your time!

Industry/Entity Type

Advertising

Other font styles liked:
• Museo Slab 500 and/or Trebuchet MS

Requirements
Must have
• Rivet Bundle or Rivet Bundle Snack Box
• $19.95 or for only $19.95

```html
<!DOCTYPE html>
<html lang="en">
<head>
<meta charset="utf-8">
<title>Rivet Bundle Snack Box</title>
<link rel="stylesheet" href="https://fonts.googleapis.com/css2?family=Nunito:ital,wght@0,400;1,600&family=Roboto+Slab:wght@500&display=swap">
<style>
  :root {
    --plank-blue: #4f8fa6;
    --plank-blue-dark: #3d7489;
    --plank-blue-light: #6aa6bb;
    --plank-seam: #2b4f5e;
    --board-light: #d9d6cc;
    --board-shade: #bdb8ab;
    --brand-red: #b6453d;
    --text-white: #ffffff;
    --product-warm: #c9a46a;
    --product-cool: #8fb4c4;
  }
  html, body {
    margin: 0;
    padding: 0;
    width: 1200px;
    height: 469px;
    overflow: hidden;
    background: #ffffff;
  }
  .banner {
    position: relative;
    width: 1200px;
    height: 469px;
    overflow: hidden;
    background: linear-gradient(180deg, var(--plank-blue-light) 0%, var(--plank-blue) 45%, var(--plank-blue-dark) 100%);
  }
  .planks {
    position: absolute;
    inset: 0;
  }
  .name-board {
    position: absolute;
    left: 0;
    top: 110px;
    width: 1200px;
    height: 146px;
    background: linear-gradient(180deg, var(--board-light) 0%, #cfcbc0 60%, var(--board-shade) 100%);
    border-top: 4px solid var(--plank-seam);
    border-bottom: 4px solid var(--plank-seam);
  }
  .headline-lead {
    position: absolute;
    left: 18px;
    top: -8px;
    margin: 0;
    font-family: "Nunito", sans-serif;
    font-weight: 400;
    font-size: 84px;
    line-height: 1.2;
    color: var(--text-white);
    letter-spacing: 1px;
  }
  .headline-name {
    position: absolute;
    left: 40px;
    top: 118px;
    width: 1000px;
    margin: 0;
    font-family: "Roboto Slab", serif;
    font-weight: 500;
    font-size: 132px;
    line-height: 130px;
    color: var(--brand-red);
    letter-spacing: 58px;
    white-space: nowrap;
  }
  .product-label {
    position: absolute;
    right: 16px;
    top: 270px;
    margin: 0;
    font-family: "Nunito", sans-serif;
    font-style: italic;
    font-weight: 600;
    font-size: 74px;
    line-height: 1.1;
    color: var(--text-white);
    text-align: right;
  }
  .price {
    position: absolute;
    right: 20px;
    top: 350px;
    margin: 0;
    font-family: "Nunito", sans-serif;
    font-weight: 400;
    font-size: 42px;
    line-height: 1.1;
    color: var(--text-white);
    text-align: right;
  }
  .snack-spread {
    position: absolute;
    left: 10px;
    top: 284px;
    width: 612px;
    height: 190px;
    border-radius: 10px 10px 0 0;
    background: linear-gradient(100deg, var(--product-cool) 0%, var(--product-warm) 30%, #e0d2b4 50%, var(--product-warm) 68%, #d88a9a 100%);
  }
</style>
</head>
<body>
  <div class="banner">
    <svg class="planks" width="1200" height="469" viewBox="0 0 1200 469" role="img" aria-label="Weathered blue painted wood planks">
      <line x1="0" y1="324" x2="1200" y2="324" stroke="var(--plank-seam)" stroke-width="3" opacity="0.6"/>
      <line x1="0" y1="412" x2="1200" y2="412" stroke="var(--plank-seam)" stroke-width="3" opacity="0.6"/>
    </svg>

    <div class="name-board"></div>

    <p class="headline-lead">rivet</p>
    <h1 class="headline-name">BUNDLE</h1>

    <p class="product-label">snack box</p>
    <p class="price">only $19.95</p>

    <div class="snack-spread" role="img" aria-label="Assorted single-serve snack packages from the box spread out: fruit bars, egg white chips, dried fruit and nut snacks"></div>
  </div>
</body>
</html>
```